QUELTAN PLUMBING CAR WRAP DESIGN

I want a minimalist but modern/fun design. I’ve attached some examples. It’s a Vardeno pelum van.
The car needs to be a grey, with the blue logo over it. The logo could be outlined with white or silver let’s example. The logo needs a be a bright metallic. Using bits of great would also look good.
I want the “droplet” giant on the back sides and also giant droplet on the front on an angle.
My favour example is the ‘marrowed’, car example. That’s basically what I want for our cars. It’s grey with the blue logo.
See the orange car example you could put a section of the car in blue like they have with the orange.

```html
<!DOCTYPE html>
<html lang="en">
<head>
<meta charset="utf-8">
<title>Queltan Trades Group – Van Wrap</title>
<link rel="stylesheet" href="https://fonts.googleapis.com/css2?family=Montserrat:wght@600;800&family=Roboto+Condensed:ital,wght@1,700&display=swap">
<style>
  :root {
    --bg: #ffffff;
    --body-white: #f3f4f6;
    --navy: #2b2a6e;
    --royal: #1f4fa8;
    --sky: #1f8fd6;
    --tyre: #1c1c1e;
    --rim: #b9bcc1;
    --glass: #8d9094;
    --trim: #2a2a2c;
    --shadow: rgba(0,0,0,0.35);
  }
  html, body {
    margin: 0;
    width: 1200px;
    height: 1200px;
    overflow: hidden;
    background: var(--bg);
  }
  .wrap-sheet { display: block; width: 1200px; height: 1200px; }
  .brand-name { font-family: "Montserrat", sans-serif; font-weight: 800; font-size: 50px; fill: var(--navy); letter-spacing: 3px; }
  .brand-sub { font-family: "Montserrat", sans-serif; font-weight: 600; font-size: 17px; fill: var(--navy); letter-spacing: 5px; }
  .service-line { font-family: "Montserrat", sans-serif; font-weight: 800; font-size: 15px; fill: #ffffff; letter-spacing: 2px; }
  .web-address { font-family: "Roboto Condensed", sans-serif; font-style: italic; font-weight: 700; font-size: 9.5px; fill: #ffffff; letter-spacing: 1.6px; }
  .phone-number { font-family: "Roboto Condensed", sans-serif; font-style: italic; font-weight: 700; font-size: 19px; fill: var(--navy); letter-spacing: 1px; }
</style>
</head>
<body>
<svg class="wrap-sheet" viewBox="0 0 960 960" xmlns="http://www.w3.org/2000/svg">
  <defs>
    <linearGradient id="lowerBlue" x1="0" y1="0" x2="1" y2="1">
      <stop offset="0" stop-color="#1a62c0"/>
      <stop offset="1" stop-color="#1f8fd6"/>
    </linearGradient>
    <linearGradient id="roofBlue" x1="0" y1="0" x2="1" y2="0">
      <stop offset="0" stop-color="#1f8fd6"/>
      <stop offset="1" stop-color="#1f3f9a"/>
    </linearGradient>
    <linearGradient id="roofGrey" x1="0" y1="0" x2="1" y2="0">
      <stop offset="0" stop-color="#76777a"/>
      <stop offset="1" stop-color="#4e4f52"/>
    </linearGradient>
    <linearGradient id="dropletTone" x1="0" y1="0" x2="0" y2="1">
      <stop offset="0" stop-color="#1f4fa8"/>
      <stop offset="1" stop-color="#25a0e0"/>
    </linearGradient>
    <clipPath id="vanBody">
      <path d="M182,198 L560,194 Q602,194 624,204 L704,236 Q738,252 760,276 L775,302 L778,398 L770,426 L182,426 Q168,422 168,404 L168,214 Q168,199 182,198 Z"/>
    </clipPath>

    <g id="vanSide-base">
      <ellipse class="ground-shadow" cx="472" cy="440" rx="310" ry="8" fill="var(--shadow)" opacity="0.5"/>
      <g clip-path="url(#vanBody)">
        <rect class="body-panel" x="160" y="185" width="630" height="250" fill="var(--body-white)"/>
        <path class="lower-band" d="M160,300 L300,326 L604,392 L620,440 L160,440 Z" fill="url(#lowerBlue)"/>
      </g>
    </g>

    <g id="vanSide-details">
      <g clip-path="url(#vanBody)">
        <path class="roof-accent-line" d="M340,222 L790,328 L790,334 L340,228 Z" fill="var(--sky)"/>
        <rect class="droplet-area" role="img" aria-label="Large droplet graphic on rear side" x="168" y="200" width="132" height="190" rx="60" fill="url(#dropletTone)"/>
      </g>
      <path class="service-banner" d="M300,330 L606,386 L598,412 L300,358 Z" fill="var(--navy)"/>
      <g class="side-window">
        <path d="M590,210 L662,212 Q702,226 720,258 L722,272 L594,272 Z" fill="var(--glass)"/>
        <rect x="716" y="250" width="12" height="20" rx="3" fill="var(--trim)"/>
      </g>
      <rect class="door-handle" x="596" y="292" width="16" height="5" rx="2" fill="#c9ccd0"/>
      <g class="front-end">
        <rect x="752" y="340" width="24" height="24" rx="3" fill="#e9eaec" stroke="#9a9da2"/>
        <rect x="758" y="372" width="22" height="52" rx="4" fill="var(--trim)"/>
      </g>
      <rect class="rear-bumper" x="166" y="378" width="16" height="48" rx="4" fill="var(--trim)"/>
      <rect class="rear-light" x="168" y="286" width="8" height="40" rx="2" fill="#b5242c"/>
      <g class="wheel rear">
        <path d="M252,426 A50,50 0 0 1 352,426 Z" fill="var(--trim)"/>
        <circle cx="302" cy="406" r="40" fill="var(--tyre)"/>
        <circle cx="302" cy="406" r="25" fill="var(--rim)"/>
        <circle cx="302" cy="406" r="7" fill="#7d8085"/>
      </g>
      <g class="wheel front">
        <path d="M596,426 A50,50 0 0 1 696,426 Z" fill="var(--trim)"/>
        <circle cx="646" cy="406" r="40" fill="var(--tyre)"/>
        <circle cx="646" cy="406" r="25" fill="var(--rim)"/>
        <circle cx="646" cy="406" r="7" fill="#7d8085"/>
      </g>
      <g class="brand-lockup" transform="rotate(8 330 280)">
        <text class="brand-name" x="330" y="286">QUELTAN</text>
        <text class="brand-sub" x="334" y="310">TRADES GROUP</text>
      </g>
      <g class="service-list" transform="rotate(10.4 306 352)">
        <text class="service-line" x="310" y="357">PLUMBING</text>
        <circle cx="430" cy="352" r="4" fill="var(--sky)"/>
        <text class="service-line" x="440" y="357">GAS</text>
        <circle cx="492" cy="352" r="4" fill="var(--sky)"/>
        <text class="service-line" x="502" y="357">AIR</text>
      </g>
      <text class="web-address" x="388" y="216" transform="rotate(13 388 216)">WWW.QUELTANTRADESGROUP.COM</text>
      <text class="phone-number" x="612" y="330" transform="rotate(7 612 330)">123-555-0147</text>
    </g>
  </defs>

  <g class="van van--blue-cab">
    <use href="#vanSide-base"/>
    <g clip-path="url(#vanBody)">
      <path class="cab-roof" d="M270,190 L790,190 L790,326 L340,220 Z" fill="url(#roofBlue)"/>
    </g>
    <use href="#vanSide-details"/>
  </g>

  <g class="van van--grey-cab" transform="translate(0,340)">
    <use href="#vanSide-base"/>
    <g clip-path="url(#vanBody)">
      <path class="cab-roof" d="M270,190 L790,190 L790,326 L340,220 Z" fill="url(#roofGrey)"/>
      <path class="roof-lead" d="M270,190 L430,190 L470,250 L340,220 Z" fill="var(--royal)"/>
    </g>
    <use href="#vanSide-details"/>
  </g>
</svg>
</body>
</html>
```